Business Card Design and stationary (thank you cards)

I am basically starting a "handyman" business but have a little ego issue with that term. I have been a professional in the design and construction business for 30 years. I want simple…I will define the scope of work I do as i move forward, and it can vary and i want it to vary.

Target Market(s)

Homeowners mostly

Industry/Entity Type

Business

Contact Information for Business Card

Company Name is "Tidy Corner Crew" Dale P. Whitcombe, 42 Larkvale Hollow Road, Fernbrook, Vt, 06419 (but I may want to use a PO Box), Phone is 860-555-0187, email is dwhitcombe584@mailnest.example,

Font styles to use
Sans Serif

Requirements
Should not have
• anything pre designed….hammers or whatever…custom lines to make home features as shone but simple and elegant

```html
<!DOCTYPE html>
<html lang="en">
<head>
<meta charset="utf-8">
<title>Tidy Corner Crew – Business Card</title>
<link rel="stylesheet" href="https://fonts.googleapis.com/css2?family=Ubuntu:wght@400;500;700&display=swap">
<style>
  :root {
    --page: #e9e6e1;
    --wood-light: #e8bd72;
    --wood-mid: #d9a455;
    --wood-dark: #b9803a;
    --ink: #3a2412;
    --ink-soft: #4a3019;
    --panel: #5a3517;
    --tick: #c8201e;
    --shadow: rgba(40, 25, 10, 0.25);
  }
  * { box-sizing: border-box; margin: 0; padding: 0; }
  html, body {
    width: 1200px; height: 873px; overflow: hidden;
    background: var(--page);
    font-family: "Ubuntu", sans-serif;
    color: var(--ink);
  }
  .sheet { position: relative; width: 1200px; height: 873px; }
  .card {
    position: absolute; left: 285px; width: 630px; height: 360px;
    border-radius: 4px; overflow: hidden;
    box-shadow: 0 6px 18px var(--shadow);
  }
  .card--front { top: 48px; }
  .card--back  { top: 465px; }
  .card__grain {
    position: absolute; inset: 0;
    background:
      radial-gradient(ellipse at 30% 40%, var(--wood-light) 0%, transparent 60%),
      radial-gradient(ellipse at 80% 75%, var(--wood-dark) 0%, transparent 55%),
      linear-gradient(100deg, var(--wood-mid), var(--wood-light) 45%, var(--wood-mid));
  }
  .card__content { position: absolute; inset: 0; }

  /* Brand block */
  .brand { position: absolute; display: flex; align-items: center; gap: 12px; }
  .brand__square { background: var(--panel); border-radius: 4px; flex: none; }
  .brand__name { font-weight: 700; color: var(--panel); letter-spacing: 0.02em; white-space: nowrap; }
  .card--front .brand { left: 36px; top: 34px; }
  .card--front .brand__square { width: 34px; height: 34px; }
  .card--front .brand__name { font-size: 22px; }

  /* Front */
  .holder {
    position: absolute; right: 36px; top: 40px;
    font-size: 24px; font-weight: 500; color: var(--ink); white-space: nowrap;
  }
  .contact {
    position: absolute; left: 36px; top: 112px;
    list-style: none; display: flex; flex-direction: column; gap: 12px;
  }
  .contact__item {
    display: flex; align-items: center; gap: 14px;
    font-size: 19px; color: var(--ink-soft); white-space: nowrap;
  }
  .contact__icon { width: 26px; height: 26px; flex: none; }
  .tagline {
    position: absolute; left: 36px; top: 248px;
    font-size: 26px; font-weight: 700; color: var(--ink); white-space: nowrap;
  }
  .services {
    position: absolute; left: 36px; top: 292px;
    list-style: none; display: flex; flex-direction: column; gap: 6px;
  }
  .services__item {
    display: flex; align-items: center; gap: 8px;
    font-size: 14px; color: var(--ink-soft); white-space: nowrap;
  }
  .services__tick { width: 14px; height: 12px; flex: none; }

  /* Back */
  .card--back .brand { left: 90px; top: 110px; gap: 18px; }
  .card--back .brand__square { width: 70px; height: 70px; border-radius: 8px; }
  .card--back .brand__name { font-size: 40px; }
  .card--back .tagline { left: auto; right: 60px; top: 270px; font-size: 30px; }
</style>
</head>
<body>
<main class="sheet">

  <section class="card card--front" aria-label="Business card front">
    <div class="card__grain" role="img" aria-label="Light pine wood grain texture"></div>
    <div class="card__content">
      <div class="brand">
        <span class="brand__square"></span>
        <span class="brand__name">Dale P. Whitcombe</span>
      </div>
      <p class="holder">Dale P. Whitcombe</p>

      <ul class="contact">
        <li class="contact__item">
          <svg class="contact__icon" viewBox="0 0 26 26" aria-hidden="true">
            <circle cx="13" cy="13" r="12" fill="var(--ink)"/>
            <path d="M9 7l3 3-1.6 1.8c.8 1.8 2 3 3.8 3.8L16 14l3 3-1.8 2C12 19 7 14 7 8.8z" fill="var(--wood-light)"/>
          </svg>
          860-555-0187
        </li>
        <li class="contact__item">
          <svg class="contact__icon" viewBox="0 0 26 26" aria-hidden="true">
            <circle cx="13" cy="13" r="12" fill="var(--ink)"/>
            <rect x="7" y="8.5" width="12" height="9" rx="1" fill="none" stroke="var(--wood-light)" stroke-width="1.5"/>
            <path d="M7 9l6 5 6-5" fill="none" stroke="var(--wood-light)" stroke-width="1.5"/>
          </svg>
          dwhitcombe584@mailnest.example
        </li>
        <li class="contact__item">
          <svg class="contact__icon" viewBox="0 0 26 26" aria-hidden="true">
            <circle cx="13" cy="13" r="12" fill="var(--ink)"/>
            <path d="M13 6a4.5 4.5 0 0 1 4.5 4.5c0 3.4-4.5 9-4.5 9s-4.5-5.6-4.5-9A4.5 4.5 0 0 1 13 6z" fill="var(--wood-light)"/>
            <circle cx="13" cy="10.5" r="1.7" fill="var(--ink)"/>
          </svg>
          42 Larkvale Hollow Road, Fernbrook, Vt, 06419
        </li>
      </ul>

      <p class="tagline">Tidy Corner Crew</p>

      <ul class="services">
        <li class="services__item">
          <svg class="services__tick" viewBox="0 0 14 12" aria-hidden="true"><path d="M1 6l4 4 8-9" fill="none" stroke="var(--tick)" stroke-width="2.4"/></svg>
          No job too big or small
        </li>
        <li class="services__item">
          <svg class="services__tick" viewBox="0 0 14 12" aria-hidden="true"><path d="M1 6l4 4 8-9" fill="none" stroke="var(--tick)" stroke-width="2.4"/></svg>
          Home improvements, maintenance and repairs
        </li>
      </ul>
    </div>
  </section>

  <section class="card card--back" aria-label="Business card back">
    <div class="card__grain" role="img" aria-label="Light pine wood grain texture"></div>
    <div class="card__content">
      <div class="brand">
        <span class="brand__square"></span>
        <span class="brand__name">Dale P. Whitcombe</span>
      </div>
      <p class="tagline">Tidy Corner Crew</p>
    </div>
  </section>

</main>
</body>
</html>
```